Kelton Produce and Landscape Supplies

We require a design for a new business. It is a multi purpose business that supplies Animal foods and supplies for farmers as well as for pets focusing on horses. We also provide landscape materials, Gravels, Sands, Soils, mulches, garden furniture, water features, statues etc. Attached to the business is a new cafe called the "Mapleview Cafe". We have a small gift shop, post office and general store on the premises. To add to the challenge we have farmyard animals like goats, pigs, chickens, ducks, cows, miniature horse along with rabbits, dogs, cats, snakes and birds. I would like to market the total business over both sides of the flyer. Perhaps the Produce and Landscape Supplies on one side and the Cafe and gifts shop etc on the reverse? I have attached a entrance sign that we recently had designed. The Cow is going to be our main character as we are located in dairy farm country.

Industry/Entity Type

Business

```html
<!DOCTYPE html>
<html lang="en">
<head>
<meta charset="utf-8">
<title>Kelton Produce and Landscape Supplies – Flyer</title>
<link href="https://fonts.googleapis.com/css2?family=Special+Elite&family=Oswald:wght@300;400&family=Jost:wght@400&display=swap" rel="stylesheet">
<style>
  :root {
    --backdrop: #232323;
    --sky-top: #1f78d6;
    --sky-light: #8fd0f4;
    --grass: #3fa42a;
    --grass-dark: #2a7d1c;
    --panel-light: #eefafb;
    --panel-teal: #43c3cf;
    --band-teal: #1a7f96;
    --ink: #262b2f;
    --ink-soft: #2f3a40;
    --white: #ffffff;
    --frame-grey: #6d6e70;
    --leaf-green: #8ccf6a;
    --leaf-pale: #eef7e6;
    --water-blue: #4cb0e6;
    --water-pale: #d9f0fb;
    --slate-teal: #2f5f6b;
  }
  * { box-sizing: border-box; margin: 0; padding: 0; }
  html, body { width: 900px; height: 1200px; overflow: hidden; background: var(--backdrop); }
  .canvas { position: relative; width: 900px; height: 1200px; }

  .flyer-side { position: absolute; left: 72px; width: 756px; height: 535px; overflow: hidden; }
  .flyer-side--produce { top: 53px; }
  .flyer-side--cafe { top: 626px; height: 534px; }
  .side-backdrop { position: absolute; inset: 0; width: 100%; height: 100%; }

  /* produce side */
  .business-name {
    position: absolute; left: 150px; top: 38px; width: 330px;
    font-family: "Special Elite", "Courier New", monospace;
    font-size: 28px; line-height: 42px; color: var(--ink); text-align: center;
  }
  .phone {
    position: absolute; right: 38px; top: 56px;
    display: flex; align-items: center; gap: 10px;
    font-family: "Jost", Arial, sans-serif; font-size: 31px; color: var(--white);
  }
  .phone svg { width: 30px; height: 30px; }
  .photo-frame {
    position: absolute; left: 50px; top: 172px; width: 332px; height: 332px;
    border-radius: 50%; background: var(--frame-grey); padding: 12px;
  }
  .photo-fill {
    width: 100%; height: 100%; border-radius: 50%;
    background: radial-gradient(circle at 40% 45%, #3a3a3a 0%, #1c1c1c 45%, #8a6a45 80%, #a88457 100%);
  }
  .headline {
    position: absolute; right: 40px; top: 160px; text-align: right;
    font-family: "Oswald", "Arial Narrow", sans-serif; font-weight: 300;
    font-size: 45px; line-height: 59px; color: var(--ink);
  }
  .landscape-lead {
    position: absolute; right: 38px; top: 343px; text-align: right;
    font-family: "Jost", Arial, sans-serif; font-size: 30px; line-height: 40px; color: var(--ink);
  }
  .landscape-list {
    position: absolute; right: 38px; top: 430px; text-align: right;
    font-family: "Oswald", "Arial Narrow", sans-serif; font-weight: 300;
    font-size: 16px; line-height: 25px; color: var(--ink);
  }

  /* cafe side */
  .cafe-name {
    position: absolute; left: 38px; top: 42px;
    font-family: "Special Elite", "Courier New", monospace;
    font-size: 34px; color: var(--ink);
  }
  .cafe-tagline {
    position: absolute; right: 36px; top: 44px;
    font-family: "Special Elite", "Courier New", monospace;
    font-size: 30px; color: var(--ink);
  }
  .mascot-ring {
    position: absolute; left: 438px; top: 108px; width: 226px; height: 226px;
    border-radius: 50%; background: var(--band-teal); padding: 9px;
  }
  .mascot-fill {
    width: 100%; height: 100%; border-radius: 50%;
    background: radial-gradient(circle at 50% 45%, #f4f4f4 0%, #b9bcbe 55%, #6f7376 100%);
  }
  .animals-heading {
    position: absolute; left: 48px; top: 196px;
    font-family: "Oswald", "Arial Narrow", sans-serif; font-weight: 300;
    font-size: 34px; color: var(--ink-soft);
  }
  .animals-list {
    position: absolute; left: 48px; top: 254px;
    font-family: "Jost", Arial, sans-serif; font-size: 28px; line-height: 36px; color: var(--ink-soft);
  }
  .contact-label {
    position: absolute; left: 48px; top: 486px;
    font-family: "Jost", Arial, sans-serif; font-size: 22px; color: var(--ink-soft);
  }
</style>
</head>
<body>
<main class="canvas">

  <section class="flyer-side flyer-side--produce">
    <svg class="side-backdrop" viewBox="0 0 756 535" preserveAspectRatio="none" aria-hidden="true">
      <defs>
        <linearGradient id="sky" x1="0" y1="0" x2="1" y2="0.6">
          <stop offset="0" stop-color="var(--sky-light)"/>
          <stop offset="0.6" stop-color="var(--sky-top)"/>
          <stop offset="1" stop-color="#0f5fc4"/>
        </linearGradient>
        <linearGradient id="grass" x1="0" y1="0" x2="0" y2="1">
          <stop offset="0" stop-color="var(--grass)"/>
          <stop offset="1" stop-color="var(--grass-dark)"/>
        </linearGradient>
        <linearGradient id="panel" x1="0" y1="0" x2="1" y2="0.3">
          <stop offset="0" stop-color="var(--panel-light)"/>
          <stop offset="1" stop-color="var(--panel-teal)"/>
        </linearGradient>
      </defs>
      <rect width="756" height="535" fill="url(#sky)"/>
      <rect y="410" width="756" height="125" fill="url(#grass)"/>
      <path d="M250 215 Q 480 120 756 138 L756 505 Q 540 520 330 470 Z" fill="var(--white)"/>
      <path d="M258 222 Q 480 132 756 150 L756 492 Q 540 505 330 462 Z" fill="url(#panel)"/>
      <path d="M330 470 Q 540 520 756 505 L756 515 Q 540 530 330 478 Z" fill="var(--band-teal)"/>
    </svg>

    <h1 class="business-name">KELTON PRODUCE &amp;<br>LANDSCAPE SUPPLIES</h1>

    <p class="phone">
      <svg viewBox="0 0 30 30" aria-hidden="true">
        <circle cx="15" cy="15" r="13" fill="none" stroke="var(--white)" stroke-width="2.2"/>
        <path d="M10 8 l3 0 l1.5 4 l-2 1.5 q1.5 3.5 4 5 l1.5 -2 l4 1.5 l0 3 q-1 1.5 -3 1.5 q-10 -2 -11 -12 q0 -2 2 -2.5 Z" fill="var(--white)"/>
      </svg>
      6550 4817
    </p>

    <div class="photo-frame">
      <div class="photo-fill" role="img" aria-label="Photo of dairy cows feeding on hay"></div>
    </div>

    <h2 class="headline">ANIMAL FOODS<br>AND SUPPLIES<br>FOR FARMERS</h2>
    <p class="landscape-lead">We Also Provide<br>Landscape Materials</p>
    <p class="landscape-list">Gravels, Sands, Soils, Mulches, Garden Furniture,<br>Water Features, Statues Etc.</p>
  </section>

  <section class="flyer-side flyer-side--cafe">
    <svg class="side-backdrop" viewBox="0 0 756 534" preserveAspectRatio="none" aria-hidden="true">
      <defs>
        <linearGradient id="leaf" x1="0" y1="0" x2="1" y2="0">
          <stop offset="0" stop-color="var(--leaf-green)"/>
          <stop offset="0.55" stop-color="var(--leaf-pale)"/>
          <stop offset="1" stop-color="var(--leaf-green)"/>
        </linearGradient>
        <linearGradient id="water" x1="0" y1="0" x2="0" y2="1">
          <stop offset="0" stop-color="var(--water-blue)"/>
          <stop offset="0.5" stop-color="var(--water-pale)"/>
          <stop offset="1" stop-color="var(--water-blue)"/>
        </linearGradient>
      </defs>
      <rect width="756" height="534" fill="url(#water)"/>
      <path d="M0 0 H756 V120 Q 560 150 420 160 Q 200 130 0 148 Z" fill="url(#leaf)"/>
      <path d="M0 140 Q 200 122 420 152 Q 560 142 756 112 V122 Q 560 152 420 162 Q 200 132 0 150 Z" fill="var(--band-teal)"/>
      <path d="M640 160 Q 700 140 756 128 V390 Q 700 330 640 300 Z" fill="var(--slate-teal)"/>
      <rect y="466" width="756" height="68" fill="var(--water-blue)" opacity="0.55"/>
    </svg>

    <h1 class="cafe-name">MAPLEVIEW CAFE</h1>
    <p class="cafe-tagline">Cafe And Gifts Shop</p>

    <div class="mascot-ring">
      <div class="mascot-fill" role="img" aria-label="Cartoon cow mascot illustration"></div>
    </div>

    <h2 class="animals-heading">We Have Farmyard Animals</h2>
    <p class="animals-list">Goats, Pigs, Chickens,<br>Ducks, Cows,<br>Miniature Horse Along<br>With Rabbits,<br>Dogs, Cats, Snakes And Birds.</p>
    <p class="contact-label">Contact Info-</p>
  </section>

</main>
</body>
</html>
```